A3 Event Poster for School Fundraiser

We are looking for a bold, engaging, and professional A3 poster design to promote a special school fundraising event. A top athlete will be visiting a primary school to inspire children, encourage participation in sport, and help launch a fundraising initiative to raise money for new PE/sports equipment for the school.

The poster will be displayed prominently outside the school and shared with parents and families. Its purpose is to generate excitement, explain the event quickly, and encourage parents/families to sponsor and get involved.

We work with about 50 different athletes so will need the design to be easy to alter the picture of the athlete/name etc so it can be replicated across the different athletes.

Target Market(s)

Priamary School Parents/Communities

Industry/Entity Type

Education

Font styles to use
Other font styles liked:
• The logo font is Rajdhani. ‘Corvel’ is bold, ‘Pennix’ is semibold and the strapline is regular.

Requirements
Must have
• Space for the Event Date (that school can write in themselves), A picture of the visiting athlete and their bio (with ability to easily change)
Nice to have
• Bold, eye-catching

```html
<!DOCTYPE html>
<html lang="en">
<head>
<meta charset="UTF-8">
<title>Inspirational Athlete Visiting Our School</title>
<link rel="stylesheet" href="https://fonts.googleapis.com/css2?family=Rajdhani:wght@300;400;500;600;700&display=swap">
<style>
  :root {
    --red: #e01a2d;
    --red-deep: #c9142a;
    --frame-purple: #7a3a98;
    --ink: #0b0b0b;
    --white: #ffffff;
    --bio: #fbe3e6;
    --bg-light: #f7f6f6;
    --bg-mid: #e9e6e6;
    --photo-blue: #2f57b8;
    --photo-pale: #dfe4ee;
  }
  * { margin: 0; padding: 0; box-sizing: border-box; }
  html, body { width: 849px; height: 1200px; overflow: hidden; background: var(--white); }
  body { font-family: 'Rajdhani', sans-serif; color: var(--ink); }

  .poster { position: relative; width: 849px; height: 1200px; overflow: hidden; }

  .backdrop {
    position: absolute; inset: 0;
    background: linear-gradient(180deg, var(--bg-light) 0%, var(--bg-mid) 30%, var(--bg-light) 55%, #f1efef 100%);
  }

  .brand-name {
    position: absolute; left: 34px; top: 48px; white-space: nowrap;
    font-size: 40px; font-weight: 600; line-height: 1; color: var(--ink);
  }

  .headline { position: absolute; left: 41px; top: 0; font-weight: 700; line-height: 1; white-space: nowrap; }
  .headline span { position: absolute; left: 0; }
  .headline .line-small { font-size: 47px; letter-spacing: 1px; }
  .headline .line-big { font-size: 88px; letter-spacing: 2px; }
  .headline .line-mid { font-size: 58px; letter-spacing: 1.5px; }

  .athlete-panel {
    position: absolute; left: 374px; top: 0; width: 426px; height: 517px;
    background: linear-gradient(180deg, var(--red-deep) 0%, var(--red) 45%, var(--red-deep) 100%);
  }
  .athlete-name {
    position: absolute; left: 374px; width: 426px; top: 205px; text-align: center;
    font-size: 40px; font-weight: 600; line-height: 1; color: var(--white); letter-spacing: 1px;
  }
  .athlete-bio {
    position: absolute; left: 404px; width: 366px; top: 275px; text-align: center;
    font-size: 18.5px; font-weight: 500; line-height: 25px; color: var(--bio);
  }

  .photo-frame { position: absolute; left: 0; top: 0; width: 849px; height: 1200px; pointer-events: none; }

  .athlete-photo {
    position: absolute; left: 353px; top: 517px; width: 496px; height: 683px;
    background: linear-gradient(135deg, var(--photo-pale) 0%, var(--photo-blue) 45%, #24408c 70%, var(--photo-pale) 100%);
  }

  .appeal {
    position: absolute; left: 33px; top: 535px;
    font-size: 30px; font-weight: 500; line-height: 41px; white-space: nowrap;
  }

  .benefit { position: absolute; left: 48px; font-size: 30px; font-weight: 500; line-height: 30px; white-space: nowrap; }
  .benefit::before {
    content: ""; position: absolute; left: -18px; top: 11px;
    width: 10px; height: 10px; border-radius: 50%; background: var(--red);
  }
  .rule { position: absolute; left: 0; height: 1.5px; background: var(--ink); }

  .event-date {
    position: absolute; left: 33px; top: 910px;
    font-size: 40px; font-weight: 600; line-height: 40px; color: var(--red);
  }

  .mission-band {
    position: absolute; left: 0; top: 1023px; width: 353px; height: 177px; background: var(--ink);
  }
  .mission-text {
    position: absolute; left: 33px; top: 1066px;
    font-size: 25px; font-weight: 300; line-height: 30px; color: var(--white); white-space: nowrap;
  }
</style>
</head>
<body>
<main class="poster">
  <div class="backdrop" role="img" aria-label="Faded photo of children playing in a school sports hall"></div>

  <div class="brand-name">Corvel Pennix</div>

  <div class="athlete-panel" role="img" aria-label="Red-tinted photo of a sports hall with a ball"></div>
  <h2 class="athlete-name">DANIEL OKORO</h2>
  <p class="athlete-bio">Daniel is a dynamic English volleyball player and coach, known for his leadership on and off the court and his passion for inspiring the next generation through sport.</p>

  <h1 class="headline">
    <span class="line-small" style="top:205px">INSPIRATIONAL</span>
    <span class="line-big" style="top:257px">ATHLETE</span>
    <span class="line-big" style="top:340px">VISITING</span>
    <span class="line-mid" style="top:432px">OUR SCHOOL</span>
  </h1>

  <div class="athlete-photo" role="img" aria-label="Portrait photo of the visiting athlete in a team tracksuit jacket"></div>

  <svg class="photo-frame" viewBox="0 0 849 1200" aria-hidden="true">
    <polyline points="849,492 323,492 323,1187 353,1187" fill="none" stroke="var(--frame-purple)" stroke-width="2.5"/>
  </svg>

  <p class="appeal">Help us raise funds for<br>new sports equipment</p>

  <div class="benefit" style="top:651px">Be inspired</div>
  <div class="rule" style="top:708px; width:182px"></div>
  <div class="benefit" style="top:732px">Make a difference</div>
  <div class="rule" style="top:780px; width:267px"></div>
  <div class="benefit" style="top:799px">Get Active</div>
  <div class="rule" style="top:844px; width:172px"></div>

  <div class="event-date">Event Date:</div>

  <div class="mission-band"></div>
  <p class="mission-text">Inspiring every child to<br>lead an active, resilient<br>and healthy life</p>
</main>
</body>
</html>
```